Kestrel Property Management email template

Looking for an email template for communications sent to residents that reads well in most email formats including mobile devices. Similar to the attached email, not quite reclaimed wood but something warm with interesting texture

```html
<!DOCTYPE html>
<html lang="en">
<head>
<meta charset="utf-8">
<title>Kestrel Property Management – Resident Newsletter</title>
<link href="https://fonts.googleapis.com/css2?family=Nunito+Sans:ital,wght@0,300;0,400;0,600;0,700;0,800;1,400&family=Ubuntu:wght@300;400&display=swap" rel="stylesheet">
<style>
  :root{
    --espresso:#2e1d14;
    --walnut:#3b2619;
    --walnut-light:#4a3020;
    --heading:#7a3a1a;
    --terracotta:#b4552a;
    --sand:#d8b88e;
    --sand-dark:#c9a577;
    --amber:#e2a866;
    --cream:#fbf6ee;
    --white:#ffffff;
    --text:#2f241c;
    --charcoal:#3a2a20;
    --grain:repeating-linear-gradient(92deg,rgba(255,255,255,.035) 0 2px,rgba(0,0,0,.05) 2px 5px,rgba(255,255,255,0) 5px 11px);
    --grain-fine:repeating-linear-gradient(88deg,rgba(0,0,0,.035) 0 1px,rgba(255,255,255,.05) 1px 4px,rgba(0,0,0,0) 4px 9px);
  }
  *{box-sizing:border-box;margin:0;padding:0}
  html,body{width:1200px;height:3730px;overflow:hidden}
  body{position:relative;font-family:"Nunito Sans",sans-serif;color:var(--text);
    background:var(--grain-fine),var(--cream)}
  .abs{position:absolute}

  /* header */
  .brand-square{left:86px;top:150px;width:134px;height:170px;background:var(--grain),var(--walnut)}
  .header-rule{left:249px;top:86px;width:2px;height:274px;background:var(--espresso)}
  .social{width:80px;height:80px;border-radius:50%;background:var(--grain),var(--walnut)}
  .brand-name{left:284px;top:192px;font-size:49px;font-weight:800;color:var(--espresso);letter-spacing:.3px;white-space:nowrap}

  /* hero */
  .hero{left:86px;top:360px;width:1028px;height:613px;
    background:linear-gradient(90deg,#8a7563 0%,#a38a73 25%,#7a4a36 55%,#8a4630 80%,#5b2e20 100%)}
  .hero-shade{left:86px;top:360px;width:1028px;height:613px;background:rgba(40,22,12,.35)}
  .hero-title{left:86px;top:470px;width:1028px;text-align:center;color:var(--white);font-weight:300;font-size:52px;line-height:62px}
  .hero-goal{left:86px;top:636px;width:1028px;text-align:center;color:var(--white);font-size:23px;font-weight:600}
  .hero-copy{left:220px;top:686px;width:760px;text-align:center;color:var(--white);font-size:22px;font-style:italic;line-height:31px}
  .pill{left:326px;width:548px;height:84px;border-radius:42px;background:var(--grain),var(--terracotta);color:var(--white);font-weight:700;font-size:23px;line-height:31px}
  .pill svg{position:absolute;left:50px;top:24px}
  .pill span{position:absolute;left:130px;top:11px}
  .hero-phone{left:86px;top:908px;width:1028px;text-align:center;color:var(--white);font-size:30px;font-weight:300}

  .nav{left:86px;top:973px;width:1028px;height:91px;background:var(--grain),var(--walnut)}
  .nav a{position:absolute;top:30px;color:var(--white);font-size:24px;text-decoration:none}

  /* intro */
  .section-title{left:86px;color:var(--heading);font-size:31px;font-weight:600}
  .intro-bar{left:102px;top:1177px;width:6px;height:263px;background:var(--terracotta)}
  .intro-copy{left:128px;top:1178px;width:980px;font-size:17.5px;line-height:24px}
  .intro-copy p+p{margin-top:24px}

  /* service cards */
  .card{width:480px;background:var(--grain),linear-gradient(160deg,var(--walnut-light),var(--walnut));color:var(--white)}
  .card-stripe{position:absolute;top:0;right:20px;width:10px;height:100%;background:var(--amber)}
  .card-icon{position:absolute;left:30px;top:20px}
  .card-title{position:absolute;left:104px;top:30px;font-size:19px;font-weight:700}
  .card-body{position:absolute;left:28px;top:90px;width:400px;font-size:15px;line-height:24px}
  .card-btn{position:absolute;left:27px;width:190px;height:42px;background:var(--terracotta);font-size:22px;font-weight:700;text-align:center;line-height:42px}

  /* contact */
  .contact{left:0;top:2730px;width:1200px;height:767px;background:var(--grain-fine),var(--sand)}
  .skyline{left:826px;top:2730px;width:374px;height:767px;
    background:linear-gradient(180deg,#e6cfae 0%,#dcc09c 35%,#9a7a5e 60%,#7d6552 85%,#5e4b3d 100%)}
  .open-title{left:82px;top:2790px;font-family:"Ubuntu",sans-serif;font-weight:300;font-size:82px;color:var(--charcoal)}
  .open-sub{left:82px;top:2886px;font-family:"Ubuntu",sans-serif;font-weight:400;font-size:51px;color:var(--charcoal)}
  .label{font-size:24px;color:var(--charcoal);display:flex;align-items:center;gap:10px}
  .value{font-size:23px;font-weight:700;color:var(--white);line-height:31px;white-space:nowrap}
  .follow{left:97px;top:3270px;font-size:22px;color:var(--text)}

  /* footer */
  .footer{left:0;top:3497px;width:1200px;height:233px;background:var(--grain),var(--espresso);color:var(--white)}
  .footer-copy{position:absolute;left:86px;top:28px;font-size:22px}
  .footer-note{position:absolute;left:86px;top:76px;font-size:18px;line-height:24px}
  .footer-note a{color:var(--amber);text-decoration:underline}
  .footer-sign{position:absolute;left:86px;top:172px;font-size:18px}
</style>
</head>
<body>

<!-- header -->
<div class="abs brand-square"></div>
<div class="abs header-rule"></div>
<div class="abs social" style="left:822px;top:87px"></div>
<div class="abs social" style="left:924px;top:87px"></div>
<div class="abs social" style="left:1026px;top:87px"></div>
<div class="abs brand-name">KESTREL PROPERTY MANAGEMENT</div>

<!-- hero -->
<div class="abs hero" role="img" aria-label="Photo of city buildings and brick apartment towers along a street"></div>
<div class="abs hero-shade"></div>
<div class="abs hero-title">LUXURY CONDOMINIUM<br>MANAGEMENT</div>
<div class="abs hero-goal">OUR GOAL</div>
<div class="abs hero-copy">To assure your property is maintained to the highest possible level and to help associations maximize income, control expenses, enhance property value and develop a long-term relationship with our clients.</div>
<div class="abs pill" style="top:806px">
  <svg width="50" height="36" viewBox="0 0 50 36"><path d="M2 14h28V4l18 14-18 14V22H2z" fill="#fff"/></svg>
  <span>KPM Featured in November 2020<br>&nbsp;Ledger Build Magazine</span>
</div>
<div class="abs hero-phone">617-555-0148</div>

<nav class="abs nav">
  <a style="left:27px">COMPANY</a>
  <a style="left:187px">MANAGEMENT</a>
  <a style="left:401px">CITY LINKS</a>
  <a style="left:567px">REGISTRATION AND REQUEST FORMS</a>
</nav>

<!-- intro -->
<h2 class="abs section-title" style="top:1116px">KESTREL PROPERTY MANAGEMENT</h2>
<div class="abs intro-bar"></div>
<div class="abs intro-copy">
  <p>Is an innovative full-service property management firm founded in 1983 by Harold T. Brennan.<br>For more than three decades, Kestrel Property Management has served thousands of clients and remained at the forefront of the property management industry, emerging as a leader in the management of condominium associations.</p>
  <p>We're not brokers. We're not leasing agents. Kestrel Property Management focuses exclusively on property management and maintenance. Our primary concern is addressing your needs.</p>
  <p>As a company, we are committed to providing our clients with sophisticated, cost-effective, and personalized property management solutions which are specific to each client. Our growth over the years is a result of our ability to deliver on this commitment.</p>
</div>

<h2 class="abs section-title" style="top:1492px">TECH-FORWARD MANAGEMENT</h2>

<!-- cards -->
<div class="abs card" style="left:86px;top:1560px;height:267px">
  <div class="card-stripe"></div>
  <svg class="card-icon" width="60" height="60" viewBox="0 0 60 60" fill="none" stroke="#fff" stroke-width="2.5"><circle cx="30" cy="30" r="12"/><circle cx="10" cy="10" r="6"/><circle cx="50" cy="10" r="6"/><circle cx="10" cy="50" r="6"/><circle cx="50" cy="50" r="6"/></svg>
  <div class="card-title">COMMUNITY MANAGEMENT</div>
  <div class="card-body">Effective condominium management includes not only managing the association business affairs, but the community of owners as well.</div>
  <div class="card-btn" style="top:206px">More details</div>
</div>

<div class="abs card" style="left:632px;top:1560px;height:267px">
  <div class="card-stripe"></div>
  <svg class="card-icon" width="60" height="60" viewBox="0 0 60 60" fill="none" stroke="#fff" stroke-width="2.5"><rect x="8" y="6" width="36" height="46" rx="3"/><path d="M16 18h20M16 28h20M16 38h12"/></svg>
  <div class="card-title">PROPERTY MANAGEMENT</div>
  <div class="card-body">Each property is evaluated and assigned a knowledgeable manager who works directly to facilitate all aspects of management and has the support and resources of the entire KPM team.</div>
  <div class="card-btn" style="top:206px">More details</div>
</div>

<div class="abs card" style="left:87px;top:1886px;height:299px">
  <div class="card-stripe"></div>
  <svg class="card-icon" width="60" height="60" viewBox="0 0 60 60" fill="none" stroke="#fff" stroke-width="2.5"><rect x="6" y="8" width="30" height="44" rx="3"/><rect x="38" y="24" width="16" height="28" rx="2"/><circle cx="21" cy="30" r="7"/></svg>
  <div class="card-title" style="left:118px;top:26px">PROPERTY MANAGEMENT</div>
  <div class="card-body">KPM brings integrity, experience and resources to financial reporting providing accurate and timely financial information, essential to efficient property operation.</div>
  <div class="card-btn" style="top:224px">More details</div>
</div>

<div class="abs card" style="left:634px;top:1886px;height:299px">
  <div class="card-stripe"></div>
  <svg class="card-icon" width="60" height="60" viewBox="0 0 60 60" fill="none" stroke="#fff" stroke-width="2.5"><rect x="6" y="8" width="44" height="40" rx="3"/><path d="M6 18h44"/><circle cx="36" cy="36" r="8"/></svg>
  <div class="card-title" style="left:118px;top:30px">MAINTENANCE SERVICES</div>
  <div class="card-body" style="top:104px">KPM offers twenty-four hour, on-call maintenance support seven days a week. Our team is focused on providing proactive maintenance and will review the mechanical and</div>
  <div class="card-btn" style="top:224px">More details</div>
</div>

<div class="abs card" style="left:361px;top:2245px;height:276px">
  <div class="card-stripe"></div>
  <svg class="card-icon" style="left:36px" width="60" height="60" viewBox="0 0 60 60" fill="none" stroke="#fff" stroke-width="2.5"><circle cx="16" cy="40" r="10"/><circle cx="42" cy="16" r="8"/><circle cx="46" cy="44" r="6"/><path d="M24 34l12-12M36 44h4"/></svg>
  <div class="card-title" style="left:118px;top:26px">PROJECT MANAGEMENT</div>
  <div class="card-body" style="top:106px">Our managers oversee the planning, coordination, vendor and material selection, and job oversight of improvements and capital projects.</div>
  <div class="card-btn" style="top:196px">More details</div>
</div>

<div class="abs pill" style="top:2585px">
  <svg width="50" height="36" viewBox="0 0 50 36"><path d="M2 14h28V4l18 14-18 14V22H2z" fill="#fff"/></svg>
  <span>KPM Featured in Industry<br>&nbsp;Case-Study</span>
</div>

<!-- contact -->
<div class="abs contact"></div>
<div class="abs skyline" role="img" aria-label="Photo of a city skyline with tall towers"></div>
<div class="abs open-title">We are open</div>
<div class="abs open-sub">for communication</div>

<div class="abs label" style="left:86px;top:2984px">
  <svg width="26" height="26" viewBox="0 0 24 24"><path d="M6.6 10.8a15 15 0 006.6 6.6l2.2-2.2c.3-.3.7-.4 1-.2 1.1.4 2.3.6 3.6.6.6 0 1 .4 1 1V20c0 .6-.4 1-1 1A17 17 0 013 4c0-.6.4-1 1-1h3.5c.6 0 1 .4 1 1 0 1.3.2 2.5.6 3.6.1.3 0 .7-.2 1z" fill="#3b2619"/></svg>Phone</div>
<div class="abs value" style="left:86px;top:3034px">617-555-0148</div>

<div class="abs label" style="left:420px;top:2976px">
  <svg width="30" height="22" viewBox="0 0 30 22"><rect x="1" y="1" width="28" height="20" fill="#3b2619"/><path d="M1 1l14 11L29 1" stroke="#d8b88e" stroke-width="2" fill="none"/></svg>E-mail</div>
<div class="abs value" style="left:420px;top:3026px">INFO@KESTRELPM.EXAMPLE</div>

<div class="abs label" style="left:74px;top:3112px">
  <svg width="26" height="34" viewBox="0 0 24 32"><path d="M12 0a12 12 0 00-12 12c0 9 12 20 12 20s12-11 12-20A12 12 0 0012 0zm0 17a5 5 0 110-10 5 5 0 010 10z" fill="#3b2619"/></svg>Adress</div>
<div class="abs value" style="left:86px;top:3157px">48 ELM ST 210B BOSTON,<br>MA 02118</div>

<div class="abs label" style="left:412px;top:3107px">
  <svg width="32" height="32" viewBox="0 0 32 32" fill="none" stroke="#3b2619" stroke-width="2.5"><rect x="3" y="6" width="26" height="24"/><path d="M3 12h26M10 2v7M22 2v7"/><path d="M12 18h8l-5 9"/></svg>Work hour</div>
<div class="abs value" style="left:416px;top:3155px">MONDAY-FRIDAY<br>FROM 830AM TO 5PM</div>

<div class="abs follow">FOLLOW US:</div>
<div class="abs social" style="left:89px;top:3322px"></div>
<div class="abs social" style="left:192px;top:3322px"></div>
<div class="abs social" style="left:294px;top:3322px"></div>

<!-- footer -->
<footer class="abs footer">
  <div class="footer-copy">© 2006-2020 KESTREL</div>
  <div class="footer-note">You received this letter because you agreed to receive the KESTREL Newsletter.<br>To unsubscribe, please click <a>on the link</a>.<br>You can also change the settings of newsletters in your <a>personal account</a>.</div>
  <div class="footer-sign">With respect, the Kestrel team</div>
</footer>

</body>
</html>
```